Visitenkarten-Design für aufstrebendes, modernes und innovatives Elektrounternehmen
Zielgruppe
Unsere Firma ist im Bereich Elektro- und Gebäudetechnik angesiedelt.
Zielgruppe sind Privatkunden und Geschäftskunden.
Wir machen alles rund um das Thema Elektrotechnik, Elektroinstallation ....
Aufgabenstellung
Es soll ein ansprechendes modernes Design sein. Gerne auch mit Rückseite.
Wir sind ein junges aufstrebendes modernes und innovatives Unternehmen

```html
<!DOCTYPE html>
<html lang="de">
<head>
<meta charset="utf-8">
<title>Velmarn Elektro- &amp; Gebäudetechnik – Visitenkarte</title>
<link rel="stylesheet" href="https://fonts.googleapis.com/css2?family=Open+Sans:wght@400;700&family=Roboto+Condensed:wght@400&display=swap">
<style>
  :root {
    --stage: #5f5f5f;
    --paper: #ffffff;
    --olive: #bdb634;
    --olive-bright: #c4b80f;
    --teal: #0f9aae;
    --ink: #5a5a5a;
    --ink-dark: #2f2f2f;
    --faint: #f1f1f1;
  }
  html, body {
    margin: 0;
    padding: 0;
    width: 1200px;
    height: 1200px;
    overflow: hidden;
    background: var(--stage);
  }
  .canvas {
    position: relative;
    width: 1200px;
    height: 1200px;
  }
  .card {
    position: absolute;
    display: block;
    background: var(--paper);
  }
  .card--front { left: 218px; top: 64px; width: 765px; height: 467px; }
  .card--back  { left: 220px; top: 603px; width: 760px; height: 479px; }
  .brand-name { font-family: "Open Sans", sans-serif; font-weight: 700; fill: var(--ink); }
  .brand-tagline { font-family: "Open Sans", sans-serif; font-weight: 700; fill: var(--teal); }
  .holder-name { font-family: "Open Sans", sans-serif; font-weight: 400; fill: var(--ink); letter-spacing: 2px; }
  .holder-title { font-family: "Open Sans", sans-serif; font-weight: 400; fill: var(--teal); }
  .contact-text { font-family: "Roboto Condensed", sans-serif; font-weight: 400; fill: var(--ink-dark); }
  .contact-badge { fill: var(--teal); }
  .contact-glyph { fill: none; stroke: #ffffff; stroke-width: 2; stroke-linecap: round; stroke-linejoin: round; }
</style>
</head>
<body>
<main class="canvas">

  <!-- Vorderseite -->
  <svg class="card card--front" viewBox="0 0 1062 649" aria-label="Vorderseite der Visitenkarte">
    <rect width="1062" height="649" fill="var(--paper)"/>
    <circle class="backdrop-disc" cx="547" cy="325" r="262" fill="var(--faint)"/>
    <circle class="brand-dot" cx="243" cy="324" r="95" fill="var(--olive-bright)"/>
    <text class="brand-name" x="368" y="360" font-size="128" textLength="547" lengthAdjust="spacingAndGlyphs">velmarn</text>
    <text class="brand-tagline" x="405" y="405" font-size="30" textLength="480" lengthAdjust="spacingAndGlyphs">ELEKTRO- &amp; GEBÄUDETECHNIK</text>
  </svg>

  <!-- Rückseite -->
  <svg class="card card--back" viewBox="0 0 1055 665" aria-label="Rückseite der Visitenkarte">
    <rect width="1055" height="665" fill="var(--paper)"/>
    <circle class="backdrop-disc" cx="530" cy="330" r="250" fill="var(--faint)"/>

    <g class="wave wave--top">
      <path d="M405 0 C700 20 900 100 1055 255 L1055 0 Z" fill="var(--teal)"/>
      <path d="M405 0 C700 10 900 70 1055 190 L1055 0 Z" fill="var(--olive)"/>
    </g>
    <g class="wave wave--bottom">
      <path d="M0 335 C150 520 400 640 640 665 L0 665 Z" fill="var(--faint)"/>
      <path d="M0 410 C180 540 420 640 640 665 L0 665 Z" fill="var(--teal)"/>
      <path d="M0 475 C200 580 420 652 640 665 L0 665 Z" fill="var(--olive)"/>
    </g>

    <text class="holder-name" x="480" y="256" font-size="48" text-anchor="end">JONAS VELMARN</text>
    <text class="holder-title" x="480" y="289" font-size="26" text-anchor="end">Elektrotechnikermeister</text>

    <line class="divider" x1="524" y1="220" x2="524" y2="533" stroke="var(--ink)" stroke-width="2"/>

    <g class="contact contact--phone">
      <circle class="contact-badge" cx="577" cy="280" r="17"/>
      <path class="contact-glyph" d="M571 273 l3 -2 l3 5 l-2 2 q2 4 5 6 l2 -2 l5 3 l-2 3 q-8 0 -14 -15 z"/>
      <text class="contact-text" x="613" y="289" font-size="24">08150 / 473619</text>
    </g>
    <g class="contact contact--mail">
      <circle class="contact-badge" cx="577" cy="344" r="17"/>
      <rect class="contact-glyph" x="568" y="338" width="18" height="12" rx="1"/>
      <path class="contact-glyph" d="M568 338 l9 7 l9 -7"/>
      <text class="contact-text" x="612" y="353" font-size="24">info@velmarn-licht-elektro.de</text>
    </g>
    <g class="contact contact--web">
      <circle class="contact-badge" cx="577" cy="411" r="17"/>
      <circle class="contact-glyph" cx="577" cy="411" r="9"/>
      <path class="contact-glyph" d="M568 411 h18 M577 402 q-6 9 0 18 M577 402 q6 9 0 18"/>
      <text class="contact-text" x="610" y="420" font-size="24">www.velmarn-elektrotechnik.de</text>
    </g>
    <g class="contact contact--address">
      <circle class="contact-badge" cx="577" cy="481" r="17"/>
      <path d="M577 492 q-8 -9 -8 -14 a8 8 0 0 1 16 0 q0 5 -8 14 z" fill="#ffffff"/>
      <circle cx="577" cy="478" r="3" fill="var(--teal)"/>
      <text class="contact-text" x="611" y="490" font-size="24">Lindenweg 12, 86999 Haldenbrunn</text>
    </g>
  </svg>

</main>
</body>
</html>
```